Kestrel Grooming Co Box Label

I am putting together a kit made up of beard products (oils,balms etc) which i am calling a "Copperline Tonic Crate". I need to make a label for the box which includes my logo (attached) and would like a bearded man on it as well

```html
<!DOCTYPE html>
<html lang="en">
<head>
<meta charset="utf-8">
<title>Kestrel Grooming Co – Box Label Options</title>
<link rel="stylesheet" href="https://fonts.googleapis.com/css2?family=Oswald:wght@500&family=Exo+2:wght@600;700&display=swap">
<style>
  :root {
    --board-top: #161d21;
    --board-bottom: #1f2b31;
    --label-white: #ffffff;
    --wood-light: #f3dcb8;
    --wood-mid: #ecd0a6;
    --ink-brown: #2e1c08;
    --stone-light: #b3a68c;
    --stone-dark: #8c8270;
    --ink-charcoal: #2a2522;
    --paper-light: #f3ece0;
    --paper-edge: #e4d6c0;
    --ink-black: #141414;
    --beard-copper: #b5602a;
  }
  * { margin: 0; padding: 0; box-sizing: border-box; }
  html, body { width: 1200px; height: 1102px; overflow: hidden; }
  body {
    position: relative;
    background: linear-gradient(160deg, var(--board-top), var(--board-bottom));
    font-family: "Oswald", sans-serif;
  }
  .option-card { position: absolute; width: 531px; height: 442px; overflow: hidden; }
  .option-tag {
    position: absolute;
    font-family: "Exo 2", sans-serif;
    font-weight: 700;
    font-size: 31px;
    color: var(--label-white);
  }
  .artwork { position: absolute; }
  .brand-name {
    position: absolute;
    font-family: "Oswald", sans-serif;
    font-weight: 500;
    text-transform: uppercase;
    white-space: nowrap;
    letter-spacing: 0.5px;
  }
  .rule { position: absolute; height: 2px; }

  /* Option 1 – wood */
  .card-wood {
    left: 317px; top: 62px;
    background: linear-gradient(170deg, var(--wood-light) 0%, var(--wood-mid) 45%, var(--wood-light) 70%, var(--wood-mid) 100%);
  }
  .card-wood .artwork {
    left: 43px; top: 50px; width: 184px; height: 372px;
    background: var(--ink-brown);
    border-radius: 45% 45% 50% 50% / 30% 30% 60% 60%;
  }
  .card-wood .brand-name { left: 253px; top: 200px; font-size: 24px; color: var(--ink-brown); }
  .product-line {
    position: absolute; left: 272px; top: 250px;
    display: flex; align-items: center;
    font-family: "Oswald", sans-serif; font-weight: 500;
    font-size: 13px; letter-spacing: 1px; color: var(--ink-brown);
  }
  .product-line .divider { width: 2px; height: 26px; background: var(--ink-brown); margin: 0 12px; }

  /* Option 3a – stone */
  .card-stone {
    left: 30px; top: 565px;
    background: radial-gradient(ellipse at 40% 40%, var(--stone-light), var(--stone-dark));
  }
  .card-stone .artwork {
    left: 126px; top: 0; width: 264px; height: 291px;
    background: linear-gradient(180deg, #d9c9b8 0%, var(--beard-copper) 30%, #8a4420 100%);
    border-radius: 0 0 50% 50% / 0 0 40% 40%;
  }
  .card-stone .rule { background: var(--ink-charcoal); }
  .card-stone .brand-name { left: 123px; top: 345px; font-size: 30px; color: var(--ink-charcoal); }

  /* Option 3b – paper */
  .card-paper {
    left: 631px; top: 562px;
    background: radial-gradient(ellipse at 50% 45%, var(--paper-light) 60%, var(--paper-edge));
  }
  .card-paper .artwork {
    left: 21px; top: 66px; width: 232px; height: 332px;
    background: linear-gradient(150deg, var(--ink-black) 0%, #3a3632 55%, #d8cfc0 100%);
    border-radius: 45% 40% 20% 30%;
  }
  .card-paper .rule { background: var(--ink-charcoal); }
  .card-paper .brand-name { left: 279px; top: 194px; font-size: 25px; color: var(--ink-charcoal); }
  .product-stack {
    position: absolute; left: 285px; top: 278px; width: 200px;
    list-style: none; text-align: center;
    font-family: "Exo 2", sans-serif; font-weight: 600;
    font-size: 14px; color: var(--ink-charcoal);
  }
  .product-stack li { height: 37.5px; }
</style>
</head>
<body>

  <section class="option-card card-wood">
    <div class="artwork" role="img" aria-label="Dark brown silhouette of a bearded man with quiff and sunglasses"></div>
    <div class="brand-name">Kestrel Grooming Co</div>
    <div class="product-line">
      <span>OILS</span><span class="divider"></span><span>BALMS</span><span class="divider"></span><span>SHAVE SOAP</span>
    </div>
  </section>
  <div class="option-tag" style="left:890px; top:238px;">op1</div>

  <section class="option-card card-stone">
    <div class="artwork" role="img" aria-label="Illustration of a long wavy copper beard and moustache"></div>
    <div class="rule" style="left:174px; top:310px; width:182px;"></div>
    <div class="rule" style="left:123px; top:319px; width:280px; height:3px;"></div>
    <div class="brand-name">Kestrel Grooming Co</div>
    <div class="rule" style="left:119px; top:405px; width:280px; height:3px;"></div>
    <div class="rule" style="left:165px; top:414px; width:183px;"></div>
  </section>
  <div class="option-tag" style="left:252px; top:1026px;">op3</div>

  <section class="option-card card-paper">
    <div class="artwork" role="img" aria-label="Black ink engraving of a bearded man in profile with slicked-back hair"></div>
    <div class="rule" style="left:317px; top:165px; width:148px;"></div>
    <div class="rule" style="left:275px; top:172px; width:228px;"></div>
    <div class="brand-name">Kestrel Grooming Co</div>
    <div class="rule" style="left:272px; top:243px; width:228px;"></div>
    <div class="rule" style="left:310px; top:250px; width:149px;"></div>
    <ul class="product-stack">
      <li>OILS</li>
      <li>BALMS</li>
      <li>SHAVE SOAP</li>
    </ul>
  </section>
  <div class="option-tag" style="left:860px; top:1034px;">op3</div>

</body>
</html>
```